Ironvale Guard Website Design

Hello Designers. I am an agency and am helping a security company get a better look. I have a new logo and a car done up. We are looking for a fresh look using the blue and the gold. Open to a complimentary color.

Here is the old site
https://brandomirguard.example/

Here is another design for photos and everything. We weren't sold on it because we wanted to make it simple like the first one.

https://ww2.brandomirguard.example/

Attached is also the copy I would like to put on there.

I am looking for tough, competent and simple. Our customers are contruction companies, event planners etc. It has to be clean and easy.

One thing we can't provide yet is photos. We are anticipating photos of our team with arms folded beside the car, close up of the owner with a logo'd shirt on. Pictures of an Ironvale Guard job site etc. (which most of the time is construction. They also do Mall security. You can see if you want to use stock photos for now.

I wanted to get the look of the front page done first. Hoping for something really awesome. Have fun.

```html
<!DOCTYPE html>
<html lang="en">
<head>
<meta charset="utf-8">
<title>Ironvale Guard</title>
<link rel="stylesheet" href="https://fonts.googleapis.com/css2?family=Open+Sans:wght@400;600;700&family=Poppins:wght@400;500;600&family=Libre+Baskerville:wght@700&display=swap">
<style>
:root{
  --navy:#0e2038;
  --navy-deep:#0a1829;
  --navy-soft:#16294a;
  --gold:#a3802d;
  --gold-dark:#8c6c22;
  --grey-box:#edeef1;
  --ink:#1d1d1d;
  --muted:#7a7a7a;
  --white:#ffffff;
}
*{margin:0;padding:0;box-sizing:border-box}
html,body{width:1200px;height:4354px;overflow:hidden}
body{position:relative;font-family:"Poppins",sans-serif;color:var(--ink);background:var(--white)}
section,header,footer,div.topbar{position:absolute;left:0;width:1200px}
.abs{position:absolute}
h1,h2,h3,h4{font-family:"Open Sans",sans-serif;font-weight:700}

/* top bar */
.topbar{top:0;height:31px;background:var(--navy);color:var(--white);font-size:11px;font-weight:500}
.topbar .item{position:absolute;top:0;height:31px;display:flex;align-items:center;gap:8px}
.topbar .dot{width:9px;height:9px;border-radius:50%;background:var(--white);display:inline-block}
.topbar .cta{position:absolute;right:178px;top:0;width:128px;height:31px;background:var(--gold);display:flex;align-items:center;justify-content:center;font-size:10px;font-weight:600}

/* nav */
.site-header{top:31px;height:75px;background:var(--white);border-bottom:1px solid #e5e5e5}
.brand{position:absolute;left:179px;top:22px;display:flex;align-items:center;gap:7px;font-family:"Poppins",sans-serif;font-weight:600;font-size:15px;color:var(--navy)}
.brand .mark{width:12px;height:12px;background:var(--gold)}
.nav{position:absolute;top:0;height:75px;display:flex;align-items:center;font-size:12.5px;font-weight:500;color:var(--ink)}
.nav a{position:absolute;white-space:nowrap;text-decoration:none;color:inherit}
.nav a.active{color:var(--gold)}

/* hero */
.hero{top:106px;height:499px}
.hero .photo{position:absolute;inset:0;background:linear-gradient(100deg,#1c2633 0%,#2f5a8a 30%,#6fa0d0 55%,#b8c8d6 75%,#2a3e5a 100%)}
.hero .shade{position:absolute;inset:0;background:linear-gradient(180deg,rgba(8,20,38,.55),rgba(8,20,38,.15))}
.hero h1{position:absolute;top:92px;width:100%;text-align:center;color:var(--white);font-size:44px;letter-spacing:.5px}
.hero p{position:absolute;top:160px;left:400px;width:400px;text-align:center;color:var(--white);font-size:15.5px;line-height:25px}
.btn-gold{background:var(--gold);color:var(--white);display:flex;align-items:center;justify-content:center;font-weight:500}
.hero .cta{position:absolute;left:540px;top:264px;width:119px;height:29px;font-size:11.5px}
.arrow{position:absolute;top:209px;width:40px;height:40px;border-radius:50%;background:var(--white);display:flex;align-items:center;justify-content:center}

/* about */
.about{top:605px;height:461px}
.about .photo{position:absolute;left:177px;top:67px;width:323px;height:327px;background:linear-gradient(135deg,#3a3d44,#8aa0b5 55%,#2a2d33)}
.about h2{position:absolute;left:548px;top:96px;font-size:29px;color:var(--ink)}
.about p.lede{position:absolute;left:548px;top:150px;width:470px;font-size:10px;line-height:18px;color:var(--muted)}
.checklist{position:absolute;left:554px;top:215px;width:420px;display:grid;grid-template-columns:194px 194px;row-gap:6px;font-size:10px;color:var(--muted)}
.checklist li{list-style:none;display:flex;align-items:center;gap:6px}
.checklist li::before{content:"";width:7px;height:7px;border-radius:50%;background:var(--ink)}
.btn-outline{position:absolute;border:1.5px solid var(--gold);display:flex;align-items:center;justify-content:center;font-size:11.5px;font-weight:500;color:var(--ink)}

/* services */
.services{top:1066px;height:632px;background:var(--navy)}
.services h2{position:absolute;left:179px;top:112px;color:var(--white);font-size:29px;line-height:37px}
.services p.intro{position:absolute;left:179px;top:196px;width:245px;color:var(--white);font-size:11px;line-height:18px}
.card{position:absolute;width:267px;height:213px;border:1.5px solid rgba(255,255,255,.85);overflow:hidden;color:var(--white)}
.card .bg{position:absolute;inset:0}
.card h3{position:absolute;left:24px;top:54px;font-size:13.5px;font-weight:600}
.card p{position:absolute;left:22px;top:90px;width:225px;font-size:10.5px;line-height:18.5px}
.card .more{position:absolute;left:22px;top:152px;font-size:13.5px;font-weight:600;font-family:"Open Sans",sans-serif}

/* welcome */
.welcome{top:1698px;height:609px}
.welcome h2{position:absolute;top:64px;width:100%;text-align:center;font-size:29px}
.welcome p.sub{position:absolute;top:112px;left:380px;width:440px;text-align:center;font-size:10.5px;line-height:18px;color:var(--muted)}
.greybox{position:absolute;left:174px;top:212px;width:852px;height:301px;background:var(--grey-box)}
.feature{position:absolute;top:212px;width:269px;height:301px;text-align:center}
.feature h4{position:absolute;top:112px;width:100%;font-size:14px;color:var(--navy-soft);font-weight:600}
.feature p{position:absolute;top:142px;left:18px;right:18px;font-size:11px;line-height:18px;color:var(--muted)}
.feature .btn{position:absolute;left:95px;top:218px;width:82px;height:28px;font-size:8.5px;font-weight:600}
.mission{position:absolute;left:443px;top:183px;width:314px;height:358px;background:var(--gold);color:var(--white);text-align:center}
.mission h4{position:absolute;top:158px;width:100%;font-size:15px;font-weight:600}
.mission p{position:absolute;top:190px;left:26px;right:26px;font-size:11px;line-height:18.5px}
.mission .btn{position:absolute;left:116px;top:252px;width:82px;height:28px;background:var(--white);color:var(--ink);font-size:8.5px;font-weight:600;display:flex;align-items:center;justify-content:center}

/* testimonials */
.testimonials{top:2307px;height:416px}
.testimonials .photo{position:absolute;inset:0;background:linear-gradient(110deg,#2c3a4e,#4a5a70 45%,#2e3d52 70%,#1f2b3a)}
.testimonials .shade{position:absolute;inset:0;background:rgba(16,30,52,.55)}
.testimonials h2{position:absolute;top:78px;width:100%;text-align:center;color:var(--white);font-size:29px}
.quote{position:absolute;top:176px;width:460px;color:var(--white)}
.quote .avatar{position:absolute;left:0;top:0;width:93px;height:93px;border-radius:50%;background:radial-gradient(circle at 50% 40%,#e8d6c8,#9ba7b4 70%);border:2px solid var(--white)}
.quote p{position:absolute;left:108px;top:6px;width:345px;font-size:11px;line-height:15px}
.quote .name{position:absolute;left:108px;top:88px;font-family:"Open Sans",sans-serif;font-size:14.5px;font-weight:600}
.quote .role{position:absolute;left:108px;top:108px;font-size:11px}
.dots{position:absolute;top:2634px;left:583px;display:flex;gap:5px}
.dots span{width:7px;height:7px;border-radius:50%;background:var(--white)}
.dots span.on{background:var(--gold)}

/* why choose */
.why{top:2723px;height:652px}
.why h2{position:absolute;top:65px;width:100%;text-align:center;font-size:29px}
.why p.sub{position:absolute;top:117px;left:310px;width:580px;text-align:center;font-size:14px;line-height:24px;color:#333}
.reason{position:absolute;left:177px;width:400px}
.reason svg{position:absolute;left:0;top:0}
.reason h3{position:absolute;left:81px;top:0;font-size:19px;font-weight:400;white-space:nowrap}
.reason p{position:absolute;left:81px;top:34px;width:300px;font-size:11px;line-height:23px;color:#555}
.why .photo{position:absolute;left:632px;top:206px;width:568px;height:375px;background:linear-gradient(135deg,#1a1d24,#3b4350 50%,#151820)}

/* quote form */
.ask{top:3375px;height:497px}
.ask .photo{position:absolute;inset:0;background:linear-gradient(100deg,#6a5a4f,#3b4431 40%,#26301f 65%,#3e4146)}
.ask .shade{position:absolute;inset:0;background:rgba(10,14,20,.55)}
.ask h2{position:absolute;top:52px;width:100%;text-align:center;font-family:"Libre Baskerville",serif;font-size:28px;color:var(--white);letter-spacing:1px}
.field{position:absolute;border:1.5px solid var(--white);color:var(--white);font-size:10.5px;padding:9px 12px}
.ask .submit{position:absolute;left:543px;top:399px;width:113px;height:32px;font-size:11px;font-weight:600}

/* footer */
.site-footer{top:3872px;height:482px;background:var(--navy)}
.foot-brand{position:absolute;left:177px;top:104px;display:flex;align-items:center;gap:7px;color:var(--white);font-weight:600;font-size:15px}
.foot-brand .mark{width:12px;height:12px;background:var(--gold)}
.site-footer p.blurb{position:absolute;left:343px;top:96px;width:460px;color:var(--white);font-size:11px;line-height:15px}
.touch{position:absolute;left:826px;top:101px;width:149px;height:38px;border:1.5px solid var(--white);color:var(--white);font-size:11.5px;font-weight:600;display:flex;align-items:center;justify-content:center}
.contact-box{position:absolute;left:177px;top:218px;width:845px;height:155px;background:var(--navy-soft)}
.contact-box .bar{position:absolute;left:0;bottom:0;width:100%;height:12px;background:var(--gold)}
.contact-col{position:absolute;top:56px;width:240px;text-align:center;color:var(--white)}
.contact-col h4{font-family:"Poppins",sans-serif;font-size:13.5px;font-weight:600}
.contact-col span{display:block;margin-top:10px;font-size:11px}
.copyright{position:absolute;left:181px;top:452px;color:var(--white);font-size:10px}
.copyright b{font-weight:600}
.foot-social{position:absolute;right:178px;top:450px;display:flex;gap:22px}
.foot-social span{width:14px;height:14px;border-radius:50%;background:var(--white)}
</style>
</head>
<body>

<div class="topbar">
  <div class="item" style="left:178px">
    <svg width="10" height="10" viewBox="0 0 24 24"><path fill="#fff" d="M6.6 10.8a15 15 0 006.6 6.6l2.2-2.2a1 1 0 011-.25 11.4 11.4 0 003.6.57 1 1 0 011 1V20a1 1 0 01-1 1A17 17 0 013 4a1 1 0 011-1h3.5a1 1 0 011 1c0 1.25.2 2.45.57 3.6a1 1 0 01-.25 1z"/></svg>
    Call Us: (+10) 555 014 2200
  </div>
  <div class="item" style="left:380px">
    <svg width="12" height="10" viewBox="0 0 24 18"><rect x="0" y="0" width="24" height="18" rx="2" fill="#fff"/><path d="M1 1l11 9 11-9" stroke="#0e2038" stroke-width="2" fill="none"/></svg>
    Mail: office@ironvaleguard.example
  </div>
  <div class="item" style="left:682px;gap:13px"><span class="dot"></span><span class="dot"></span><span class="dot"></span><span class="dot"></span></div>
  <div class="item" style="left:808px">
    <svg width="12" height="12" viewBox="0 0 24 24"><circle cx="12" cy="12" r="11" fill="#fff"/><rect x="10.8" y="10" width="2.4" height="8" fill="#0e2038"/><circle cx="12" cy="6.6" r="1.5" fill="#0e2038"/></svg>
    &nbsp;Support
  </div>
  <div class="cta">CONTACT WITH US</div>
</div>

<header class="site-header">
  <div class="brand"><span class="mark"></span>Ironvale Guard</div>
  <nav class="nav">
    <a class="active" style="left:320px">Home</a>
    <a style="left:397px">About Us</a>
    <a style="left:492px">Services</a>
    <a style="left:586px">Service Areas</a>
    <a style="left:714px">Testimonial</a>
    <a style="left:830px">Why Choose Us</a>
    <a style="left:968px">Contact</a>
  </nav>
</header>

<section class="hero">
  <div class="photo" role="img" aria-label="Guard in uniform speaking into a radio beside a branded patrol car"></div>
  <div class="shade"></div>
  <h1>IRONVALE GUARD</h1>
  <p>Lorem Ipsum is simply dummy text of the printing and typesetting industry. Lorem Ipsum has been the industry's standard dummy text</p>
  <div class="cta btn-gold">CALL US NOW</div>
  <div class="arrow" style="left:89px"><svg width="14" height="14" viewBox="0 0 24 24"><path d="M15 4l-8 8 8 8" stroke="#0e2038" stroke-width="3.5" fill="none"/></svg></div>
  <div class="arrow" style="left:1044px"><svg width="14" height="14" viewBox="0 0 24 24"><path d="M9 4l8 8-8 8" stroke="#0e2038" stroke-width="3.5" fill="none"/></svg></div>
</section>

<section class="about">
  <div class="photo" role="img" aria-label="Guard with earpiece pointing while talking on a radio"></div>
  <h2>ABOUT IRONVALE GUARD</h2>
  <p class="lede">Lorem Ipsum is simply dummy text of the printing and typesetting industry. Lorem Ipsum has been the industry's standard dummy text ever since the 1500s, when an unknown printer took a galley of type and scrambled it .</p>
  <ul class="checklist">
    <li>Event Security</li><li>Static Security</li>
    <li>Retail Security</li><li>Security Patrols</li>
    <li>Construction Security</li><li>Retail Security</li>
    <li>Investigations</li><li>Consulting</li>
  </ul>
  <div class="btn-outline" style="left:548px;top:329px;width:124px;height:35px">Read More</div>
  <div class="btn-gold" style="position:absolute;left:692px;top:329px;width:124px;height:35px;font-size:11.5px">Contact Us</div>
</section>

<section class="services">
  <h2>SERVICES WE'RE<br>PROVIDING</h2>
  <p class="intro">Lorem Ipsum is simply dummy text of the printing and typesetting industry. Lorem Ipsum has been the industry's standard dummy text ever since the 1500s, when an unknown printer took a galley of type and</p>

  <div class="card" style="left:466px;top:88px">
    <div class="bg" role="img" aria-label="Construction site with workers" style="background:linear-gradient(135deg,#3c3f44,#5a5f55 60%,#2c2f33)"></div>
    <h3>CONTRUCTION COMPANIES</h3>
    <p>Lorem Ipsum is simply dummy text of the printing and typesetting industry. Lorem Ipsum has been the industry's</p>
    <div class="more">Read More</div>
  </div>
  <div class="card" style="left:752px;top:88px">
    <div class="bg" role="img" aria-label="Chain-link fence with a security sign" style="background:linear-gradient(135deg,#3a3a38,#5e5a48 55%,#2c2c2a)"></div>
    <h3>SECURITY PATROLS</h3>
    <p>Lorem Ipsum is simply dummy text of the printing and typesetting industry. Lorem Ipsum has been the industry's</p>
    <div class="more">Read More</div>
  </div>
  <div class="card" style="left:179px;top:337px">
    <div class="bg" role="img" aria-label="Shopping mall interior with a guard" style="background:linear-gradient(135deg,#34383f,#565c66 55%,#2a2d33)"></div>
    <h3>MALL SECURITY</h3>
    <p>Lorem Ipsum is simply dummy text of the printing and typesetting industry. Lorem Ipsum has been the industry's standard</p>
    <div class="more">Read More</div>
  </div>
  <div class="card" style="left:466px;top:337px">
    <div class="bg" role="img" aria-label="Retail store security officer" style="background:linear-gradient(135deg,#26282c,#44474d 55%,#1e2024)"></div>
    <h3>RETAIL SECURITY</h3>
    <p>Lorem Ipsum is simply dummy text of the printing and typesetting industry. Lorem Ipsum has been the industry's</p>
    <div class="more">Read More</div>
  </div>
  <div class="card" style="left:752px;top:337px">
    <div class="bg" role="img" aria-label="Event planner in a suit" style="background:linear-gradient(135deg,#2e3034,#4e4a46 55%,#232427)"></div>
    <h3 style="top:58px">EVENT PLANNER</h3>
    <p style="top:94px">Lorem Ipsum is simply dummy text of the printing and typesetting industry. Lorem Ipsum has been the industry's</p>
    <div class="more" style="top:156px">Read More</div>
  </div>
</section>

<section class="welcome">
  <h2>WELCOME TO IRONVALE GUARD</h2>
  <p class="sub">Lorem ipsum dolor sit amet, consectetur adipisicing elit, sed do eiusmod tempor incididunt ut labore et dolore magna aliqua</p>
  <div class="greybox"></div>

  <div class="feature" style="left:174px">
    <svg class="abs" style="left:112px;top:48px" width="46" height="46" viewBox="0 0 46 46" fill="none" stroke="#a3802d" stroke-width="2"><path d="M5 22L23 6l18 16"/><path d="M10 18v22h26V18"/><rect x="19" y="28" width="8" height="12"/><circle cx="23" cy="19" r="4"/></svg>
    <h4>WHO WE ARE</h4>
    <p>Lorem ipsum dolor sit amet, consectetur adipisicing elit, sed doadiadipisicing elit, sed do pisicing elit, sed do</p>
    <div class="btn btn-gold">READ MORE</div>
  </div>

  <div class="mission">
    <svg class="abs" style="left:126px;top:68px" width="62" height="62" viewBox="0 0 62 62" fill="none" stroke="#fff" stroke-width="2"><rect x="6" y="30" width="14" height="26"/><rect x="24" y="20" width="14" height="36"/><rect x="42" y="36" width="14" height="20"/><path d="M2 56h58"/><path d="M31 20V6l12 5-12 5"/></svg>
    <h4>OUR MISSION</h4>
    <p>Lorem ipsum dolor sit amet, consectetur adipisicing elit, sed do eiusmod tempor incididunt ut labore et dolore magna aliqua.</p>
    <div class="btn">READ MORE</div>
  </div>

  <div class="feature" style="left:757px">
    <svg class="abs" style="left:112px;top:48px" width="46" height="46" viewBox="0 0 46 46" fill="none" stroke="#a3802d" stroke-width="2"><rect x="6" y="20" width="10" height="20"/><rect x="18" y="14" width="10" height="26"/><rect x="30" y="22" width="10" height="18"/><circle cx="23" cy="8" r="4"/><path d="M3 40h40"/></svg>
    <h4>OUR VISION</h4>
    <p>Lorem ipsum dolor sit amet, consectetur adipisicing elit, sed doadiadipisicing elit, sed do pisicing elit, sed do</p>
    <div class="btn btn-gold">READ MORE</div>
  </div>
</section>

<section class="testimonials">
  <div class="photo" role="img" aria-label="Side view of a branded patrol car"></div>
  <div class="shade"></div>
  <h2>TESTIMONIALS</h2>
  <div class="quote" style="left:181px">
    <div class="avatar" role="img" aria-label="Client portrait"></div>
    <p>Fusce et justo iaculis, facilisis orci sed, fringilla erat. Integer tincidunt aliquet purus quis tempor. In non est a augue maximus were as faucibus. Vestibulum arcu eros, tincidunt id porttitor in, pharetra sit amet leo.</p>
    <div class="name">Owen Tallis</div>
    <div class="role">Client</div>
  </div>
  <div class="quote" style="left:668px">
    <div class="avatar" role="img" aria-label="Client portrait"></div>
    <p>Fusce et justo iaculis, facilisis orci sed, fringilla erat. Integer tincidunt aliquet purus quis tempor. In non est a augue maximus were as faucibus. Vestibulum arcu eros, tincidunt id porttitor in, pharetra sit amet leo.</p>
    <div class="name">Graham Pell</div>
    <div class="role">Client</div>
  </div>
</section>
<div class="dots abs"><span></span><span class="on"></span><span></span></div>

<section class="why">
  <h2>WHY CHOOSE US</h2>
  <p class="sub">Lorem ipsum dolor sit amet, consectetur adipisicing elit, sed do eiusmod tempor incididunt ut labore et dolore magna aliqua. Ut enim ad minim veniam, quis</p>

  <div class="reason" style="top:211px">
    <svg width="42" height="48" viewBox="0 0 42 48" fill="none" stroke="#a3802d" stroke-width="2"><path d="M11 10h20l-2-7H13z"/><circle cx="21" cy="18" r="7"/><path d="M4 46v-8a10 10 0 0110-10h14a10 10 0 0110 10v8"/><path d="M21 30v16"/></svg>
    <h3>TRAINED GUARDS</h3>
    <p>Lorem ipsum dolor sit amet, consectetur adipisicing elit, sed do eiusmod tempor incididunt ut labore et dolore magna aliqua. Ut enim ad minim veniam, quis</p>
  </div>
  <div class="reason" style="top:344px">
    <svg width="48" height="50" viewBox="0 0 48 50" fill="none" stroke="#a3802d" stroke-width="2"><rect x="3" y="4" width="22" height="44"/><rect x="8" y="10" width="12" height="10"/><circle cx="36" cy="18" r="5"/><path d="M29 48V30a7 7 0 0114 0v18"/></svg>
    <h3>EXPERIENCED GUARDS</h3>
    <p>Lorem ipsum dolor sit amet, consectetur adipisicing elit, sed do eiusmod tempor incididunt ut labore et dolore magna aliqua. Ut enim ad minim veniam,</p>
  </div>
  <div class="reason" style="top:476px">
    <svg width="50" height="52" viewBox="0 0 50 52" fill="none" stroke="#a3802d" stroke-width="2"><circle cx="16" cy="10" r="7"/><path d="M13 10l3 3 4-5"/><rect x="4" y="22" width="26" height="28"/><rect x="10" y="28" width="14" height="10"/><path d="M34 50V30l12-8"/></svg>
    <h3>LATEST SECURITY TECHNIQUES</h3>
    <p>Lorem ipsum dolor sit amet, consectetur adipisicing elit, sed do eiusmod tempor incididunt ut labore et dolore magna aliqua. Ut enim ad minim veniam,</p>
  </div>

  <div class="photo" role="img" aria-label="Guard at a desk monitoring camera screens"></div>
</section>

<section class="ask">
  <div class="photo" role="img" aria-label="Guard with an earpiece holding a radio near a gated entrance"></div>
  <div class="shade"></div>
  <h2>ASK FOR A QUOTE</h2>
  <div class="field" style="left:401px;top:137px;width:175px;height:31px">First Name *</div>
  <div class="field" style="left:624px;top:137px;width:175px;height:31px">Last Name *</div>
  <div class="field" style="left:401px;top:194px;width:175px;height:31px">E-Mail *</div>
  <div class="field" style="left:624px;top:194px;width:175px;height:31px">Phone Number *</div>
  <div class="field" style="left:401px;top:258px;width:398px;height:107px">Type Your Message Here ...</div>
  <div class="submit btn-gold">SUBMIT</div>
</section>

<footer class="site-footer">
  <div class="foot-brand"><span class="mark"></span>Ironvale Guard</div>
  <p class="blurb">Sed ut perspiciatis unde omnis iste natus error sit voluptatem accusantium doloremque laudantium, totam rem aperiam, eaque ipsa quae ab illo inventore veritatis et quasi architecto.</p>
  <div class="touch">GET IN TOUCH</div>
  <div class="contact-box">
    <div class="contact-col" style="left:2px"><h4>PHONE</h4><span>(+10) 555 014 2200</span></div>
    <div class="contact-col" style="left:272px"><h4>EMAIL</h4><span>office@ironvaleguard.example</span></div>
    <div class="contact-col" style="left:542px"><h4>ADDRESS</h4><span>48 Harlow Yard, Brennock - 204719</span></div>
    <div class="bar"></div>
  </div>
  <div class="copyright">Copyright @ 2022 <b>Ironvale Guard</b> | All rights reserved.</div>
  <div class="foot-social"><span></span><span></span><span></span></div>
</footer>

</body>
</html>
```